Design a menu for health restaurant

A health food restaurant in Los Angeles is seeking menu design. Our foods are made from scratch using whole ingredients.
Name: Grubb Larder
Address: 1000 E 60th StLos Angeles, CA 90247
Website: www.GrubbLarder.example
We are looking for a clean and simple menu. Brand colors are white/tan, green and orange.

Please see attached excel with menu items and logo. We do not yet have prices.

Colors
f78f20
9bcb3c
ffffff
fff3d1

Requirements
Must have
• Easy to read.
Trifold menu design (front and back).
VEGAN, VEGETARIAN, GLUTEN FREE, CONTAINS NUTS symbols.
Logo.
Nice to have
• Incorporate brand colors, but still be easy to read.
We would like to use the Belco font (attached) if it works. If not we are open to a similar font that is easy to read.

Please see attached images.
We like the images and headers of OPTION 1. Would like something similar in trifold format.
We like the clean fonts of OPTION 2.

```html
<!DOCTYPE html>
<html lang="en">
<head>
<meta charset="utf-8">
<title>Grubb Larder – Trifold Menu</title>
<link href="https://fonts.googleapis.com/css2?family=Lato:wght@300;400;700;900&family=Roboto+Condensed:wght@700&family=Oswald:wght@500&display=swap" rel="stylesheet">
<style>
:root{
  --orange:#f47b20;
  --orange-soft:#f78f20;
  --green:#8dc63f;
  --green-dark:#3f9b3a;
  --ink:#3d3d3d;
  --paper:#fbfbfa;
  --paper-edge:#e9e9e7;
  --stage:#d9d9d9;
}
*{box-sizing:border-box;margin:0;padding:0}
html,body{width:879px;height:1200px;overflow:hidden}
body{background:var(--stage);font-family:"Lato",sans-serif;color:var(--ink);position:relative}
.spread{position:absolute;left:122px;width:648px;height:502px;display:flex;background:var(--paper);box-shadow:0 8px 12px -4px rgba(0,0,0,.35)}
.spread.outer{top:68px}
.spread.inner{top:623px}
.panel{width:216px;height:100%;padding:11px 7px 8px 12px;overflow:hidden;position:relative;
  background:linear-gradient(90deg,var(--paper-edge) 0,var(--paper) 6%,#fff 50%,var(--paper) 93%,var(--paper-edge) 100%)}
.section-head{width:143px;height:20px;margin:0 0 6px 24px;border-radius:10px;background:var(--orange);color:#fff;
  font-weight:300;font-size:13px;text-align:center;line-height:20px;letter-spacing:.2px;box-shadow:0 5px 5px -3px rgba(90,140,200,.35)}
.section-head.gap{margin-top:6px}
.item{display:flex;gap:5px;margin-bottom:4px}
.item-body{flex:1;min-width:0}
.item-title{display:flex;align-items:flex-end;font-size:7.4px;color:var(--orange);text-transform:uppercase;line-height:1.2;white-space:nowrap}
.item-title .dots{flex:1;border-bottom:1px dotted var(--orange);margin:0 1px 2px}
.item-desc{font-size:6.3px;line-height:1.32;font-weight:400;text-align:justify}
.tags{width:14px;flex:none;display:flex;flex-direction:column;gap:3px;padding-top:1px}
.tag{width:13px;height:13px;border-radius:50%;border:1.5px solid var(--green);position:relative;background:#fff}
.tag::after{content:"";position:absolute;inset:2.5px;border-radius:50%}
.tag.vegan::after{background:var(--orange)}
.tag.veg::after{background:var(--green)}
.tag.gf{border-color:var(--orange)}
.tag.gf::after{background:var(--green-dark);inset:3.5px}
.tag.nuts::after{background:var(--orange-soft);border-radius:40%;inset:3px 4px}
.photo-row{display:flex;gap:9px;margin:6px 0 4px 10px}
.photo{width:84px;height:62px;border:2px solid #fff;box-shadow:2px 2px 0 #c9e3a6,0 1px 3px rgba(0,0,0,.2)}
.ph-toast{background:linear-gradient(135deg,#e8e4dc,#9bbf5a 45%,#d9534f 70%,#efece6)}
.ph-cookie{background:linear-gradient(135deg,#dcdcdc,#4a3326 45%,#c79a5d 70%,#e6e6e6)}
.ph-wrap{background:linear-gradient(135deg,#f1f1f1,#3e7b35 40%,#d6a14e 65%,#f3f3f3)}
.ph-salad{background:linear-gradient(135deg,#ececec,#5d8c2f 40%,#c44a6a 65%,#eaeaea)}
.ph-bowl{background:linear-gradient(135deg,#efefef,#c8553d 40%,#6e9b3a 65%,#efefef)}
.ph-soup{background:linear-gradient(135deg,#efefef,#d98f3a 40%,#a9c25a 65%,#f0f0f0)}
.web-bar{position:absolute;left:20px;bottom:0;width:174px;height:29px;background:var(--green);border-radius:14px 14px 0 0;
  color:#fff;font-weight:700;font-size:11px;text-align:center;line-height:29px}
/* cover */
.cover{padding:0;display:flex;flex-direction:column;align-items:center}
.cover-photo{width:100%;height:310px;flex:none;position:relative;
  background:radial-gradient(circle at 50% 42%,#efe9df 0 24%,#6b8f3b 40%,#4b2f2c 64%,#3a2622 100%)}
.cover-curve{position:absolute;left:0;bottom:0;width:216px;height:60px}
.brand{position:relative;margin-top:-112px;width:124px;height:124px;border-radius:50%;background:#fff;border:2px solid var(--orange);
  display:flex;flex-direction:column;align-items:center;justify-content:center;gap:7px}
.brand-dot{width:50px;height:50px;border-radius:50%;background:var(--orange)}
.brand-name{font-weight:400;font-size:11px;color:var(--orange);letter-spacing:.5px}
.headline{margin-top:12px;font-family:"Roboto Condensed",sans-serif;font-weight:700;color:var(--orange);font-size:18.5px;line-height:1.05;text-align:center}
.cover-rule{width:128px;height:1px;background:#999;margin:6px 0}
.tagline{font-size:8.6px;color:#666;text-align:center;line-height:1.25;padding:0 10px}
.phone-bar{position:absolute;bottom:0;left:22px;width:174px;height:29px;background:var(--green);border-radius:14px 14px 0 0;
  display:flex;align-items:center;justify-content:center;gap:6px;color:#fff;font-family:"Oswald",sans-serif;font-weight:500;font-size:17px}
/* combos */
.combos{margin-top:8px;margin-left:-4px;margin-right:-7px;background:var(--green);border-radius:12px 0 0 0;display:flex;padding:8px 8px 8px 5px;gap:6px;color:#fff;height:93px}
.combos-label{writing-mode:vertical-rl;transform:rotate(180deg);font-weight:300;font-size:11px;letter-spacing:1px;text-align:center;
  border:1px solid rgba(255,255,255,.7);border-radius:9px;padding:4px 2px}
.combos .item{margin-bottom:5px}
.combos .item-title{color:#fff}
.combos .item-title .dots{border-color:#fff}
.combos .item-desc{font-size:5.8px;font-weight:300}
</style>
</head>
<body>

<section class="spread outer">
  <div class="panel">
    <h2 class="section-head">BREAKFAST</h2>
    <div class="item"><div class="item-body"><div class="item-title">Pastries<span class="dots"></span>11.99</div><p class="item-desc">Croissant (regular, almond, chocolate) Blueberry Muffin, Superseed Cookie</p></div><div class="tags"><i class="tag veg"></i></div></div>
    <div class="item"><div class="item-body"><div class="item-title">Parfait<span class="dots"></span>11.99</div><p class="item-desc">Fresh strawberries and blueberries on yogurt and muesli and topped with honey drizzle.</p></div><div class="tags"><i class="tag veg"></i></div></div>
    <div class="item"><div class="item-body"><div class="item-title">Avocado Super Toas<span class="dots"></span>11.99</div><p class="item-desc">Avocado Mash, Tomato, Basil, Ground Flax, Hemp Seed, Chickpeas, and Moringa Powder on Whole Wheat Bread.</p></div><div class="tags"><i class="tag vegan"></i></div></div>
    <div class="item"><div class="item-body"><div class="item-title">Brunch Burger<span class="dots"></span>11.99</div><p class="item-desc">House seasoned beef burger topped with an over medium egg, red leaf lettuce, tomato, housemade pickles and Larder Sauce on a bun.</p></div><div class="tags"></div></div>
    <div class="item"><div class="item-body"><div class="item-title">Breakfast Sammy<span class="dots"></span>11.99</div><p class="item-desc">Your choice of over medium egg or tofu steak with guacamole, tomato, and Larder sauce on an English muffin.</p></div><div class="tags"><i class="tag vegan"></i></div></div>
    <div class="item"><div class="item-body"><div class="item-title">AM Burrito<span class="dots"></span>11.99</div><p class="item-desc">Scrambled eggs, onion, red bell pepper, black beans, housemade salsa, yogurt, and pepper jack cheese in a tortilla.</p></div><div class="tags"><i class="tag veg"></i></div></div>
    <div class="photo-row"><div class="photo ph-toast" role="img" aria-label="Photo of avocado toast topped with strawberries"></div><div class="photo ph-cookie" role="img" aria-label="Photo of chocolate chip cookies"></div></div>
    <h2 class="section-head gap">DESSERTS</h2>
    <div class="item"><div class="item-body"><div class="item-title">Date Coffee Cake<span class="dots"></span>11.99</div><p class="item-desc">Signature date coffee cake with walnuts.</p></div><div class="tags"><i class="tag vegan"></i><i class="tag nuts"></i></div></div>
    <div class="item"><div class="item-body"><div class="item-title">Fruit + Spices<span class="dots"></span>11.99</div><p class="item-desc">Strawberry, pineapple, green apple, orange, and blueberries with lime and chili seasoning.</p></div><div class="tags"><i class="tag vegan"></i><i class="tag gf"></i></div></div>
    <div class="item"><div class="item-body"><div class="item-title">Cookies<span class="dots"></span>11.99</div><p class="item-desc">Your choice of Chocolate Chip or Double Chocolate Chip fresh baked cookie.</p></div><div class="tags"><i class="tag veg"></i></div></div>
    <div class="item"><div class="item-body"><div class="item-title">Larder Chocolate Mousse<span class="dots"></span>11.99</div><p class="item-desc">Served with grated dark chocolate.</p></div><div class="tags"><i class="tag vegan"></i><i class="tag gf"></i></div></div>
  </div>

  <div class="panel">
    <h2 class="section-head">SMOOTHIES</h2>
    <div class="item"><div class="item-body"><div class="item-title">Green Machine Smoothie<span class="dots"></span>11.99</div><p class="item-desc">Romaine, spinach, banana, mango, pineapple, flaxmilk, spirulina, almond butter.</p></div><div class="tags"><i class="tag gf"></i><i class="tag vegan"></i><i class="tag nuts"></i></div></div>
    <div class="item"><div class="item-body"><div class="item-title">Acai Smoothie<span class="dots"></span>11.99</div><p class="item-desc">Acai, blueberries, banana, pineapple, Macqui berry, flaxmilk, almond butter.</p></div><div class="tags"><i class="tag gf"></i><i class="tag vegan"></i><i class="tag nuts"></i></div></div>
    <div class="item"><div class="item-body"><div class="item-title">Mango Smoothie<span class="dots"></span>11.99</div><p class="item-desc">Mango, flaxmilk, banan, hemp seeds</p></div><div class="tags"><i class="tag gf"></i><i class="tag vegan"></i></div></div>
    <h2 class="section-head gap">DRINKS</h2>
    <div class="item"><div class="item-body"><div class="item-title">Coffeen<span class="dots"></span>11.99</div><p class="item-desc">We proudly serve Ridgeway Coffee, a local roaster.</p></div><div class="tags"></div></div>
    <div class="item"><div class="item-body"><div class="item-title">Power Date Shake<span class="dots"></span>11.99</div><p class="item-desc">Ice-blended energy smoothie featuring dates and coffee.</p></div><div class="tags"><i class="tag gf"></i><i class="tag vegan"></i></div></div>
    <div class="item"><div class="item-body"><div class="item-title">Heart Beet Juice<span class="dots"></span>11.99</div><p class="item-desc">Red beet, apple, carrot, ginger, parsley, and lemon.</p></div><div class="tags"><i class="tag gf"></i><i class="tag vegan"></i></div></div>
    <div class="item"><div class="item-body"><div class="item-title">Green Leafy Juice<span class="dots"></span>11.99</div><p class="item-desc">Spinach, kale, cucumber, apple, and oranges.</p></div><div class="tags"><i class="tag gf"></i><i class="tag vegan"></i></div></div>
    <div class="item"><div class="item-body"><div class="item-title">Fireshot<span class="dots"></span>11.99</div><p class="item-desc">Ginger and lemon shot topped with cayenne.</p></div><div class="tags"><i class="tag gf"></i><i class="tag vegan"></i></div></div>
    <div class="item"><div class="item-body"><div class="item-title">Lemonade<span class="dots"></span>11.99</div><p class="item-desc">House Made Lemonade. Choice of unsweetened or agave sweetened in Regular, Raspberry, and Lavender flavors.</p></div><div class="tags"></div></div>
    <div class="item"><div class="item-body"><div class="item-title">Tea<span class="dots"></span>11.99</div><p class="item-desc">Hot or iced.</p></div><div class="tags"></div></div>
    <div class="item"><div class="item-body"><div class="item-title">Bottled Drinks<span class="dots"></span>11.99</div><p class="item-desc">Hollow Oak kombucha (Orchard Trilogy, Orchard Gingerberry, Orchard Mango) Brightwell (Orange Mango, Lemon, Grapefruit) Palmgrove Original Sparkling Water (Stillmere) Still Water (Stillmere)</p></div><div class="tags"></div></div>
    <div class="web-bar">www.grubblarder.example</div>
  </div>

  <div class="panel cover">
    <div class="cover-photo" role="img" aria-label="Photo of egg and greens frittata bites on a plate with fresh herbs and a wooden spoon">
      <svg class="cover-curve" viewBox="0 0 216 60" preserveAspectRatio="none"><path d="M0 38 Q110 0 216 18 L216 60 L0 60Z" fill="#fff"/><path d="M0 38 Q110 0 216 18" fill="none" stroke="#8dc63f" stroke-width="5"/></svg>
    </div>
    <div class="brand"><span class="brand-dot"></span><span class="brand-name">GRUBB LARDER</span></div>
    <h1 class="headline">NATURAL FOOD<br>DELIVERED</h1>
    <div class="cover-rule"></div>
    <p class="tagline">Every meal is made from scratch with your well-being in mind. Order takeout or delivery.</p>
    <div class="phone-bar"><svg width="14" height="16" viewBox="0 0 14 16"><rect x="3" y="1" width="8" height="14" rx="2" fill="none" stroke="#fff" stroke-width="1.6"/><circle cx="7" cy="12" r="1" fill="#fff"/></svg>(555) 014-2290</div>
  </div>
</section>

<section class="spread inner">
  <div class="panel">
    <h2 class="section-head">BOWLS</h2>
    <div class="item"><div class="item-body"><div class="item-title">Southwest Bowl<span class="dots"></span>11.99</div><p class="item-desc">Your choice of protein with corn, black beans, red onions, almonds and avocado over quinoa with lime hot sauce.</p></div><div class="tags"><i class="tag gf"></i><i class="tag nuts"></i></div></div>
    <div class="item"><div class="item-body"><div class="item-title">Chimi Bowl<span class="dots"></span>11.99</div><p class="item-desc">Your choice of protein with red bell pepper, mushrooms, zucchini, squash, onion, cherry tomatoes and fresh herb chimichurri on wild and brown rice.</p></div><div class="tags"><i class="tag gf"></i></div></div>
    <div class="item"><div class="item-body"><div class="item-title">Soba Noodle Bowl<span class="dots"></span>11.99</div><p class="item-desc">Your choice of protein with spinach, snow peas, roasted carrots, red bell pepper, cilantro, sesame seeds and ginger lime sauce over soba noodles.</p></div><div class="tags"></div></div>
    <div class="item"><div class="item-body"><div class="item-title">Hollywood Bowl<span class="dots"></span>11.99</div><p class="item-desc">Your choice of protein with broccoli, roasted corn, cherry tomatoes, basil, pepitas, flax seeds and lemon juice on wild and brown rice.</p></div><div class="tags"><i class="tag gf"></i></div></div>
    <div class="item"><div class="item-body"><div class="item-title">Larder Bowl<span class="dots"></span>11.99</div><p class="item-desc">Your choice of protein with roasted chickpeas and cauliflower, zesty fennel salad and citrus yogurt.</p></div><div class="tags"><i class="tag gf"></i></div></div>
    <div class="item"><div class="item-body"><div class="item-title">Buddha Bowl<span class="dots"></span>11.99</div><p class="item-desc">Your choice of protein with corn, red kale, sweet potatoes, red cabbage, parsley, oregano, hummus, and farro.</p></div><div class="tags"></div></div>
    <div class="item"><div class="item-body"><div class="item-title">Chili Rice Bowl<span class="dots"></span>11.99</div><p class="item-desc">Chicken, onions, bell peppers, jalapeños, black &amp; kidney beans, and tomato over brown rice.</p></div><div class="tags"><i class="tag gf"></i></div></div>
    <h2 class="section-head gap">SOUPS</h2>
    <div class="item"><div class="item-body"><div class="item-title">Chicken Noodle<span class="dots"></span>11.99</div><p class="item-desc">Chicken, egg noodles, root vegetables, oregano &amp; peppercorns.</p></div><div class="tags"><i class="tag gf"></i></div></div>
    <div class="item"><div class="item-body"><div class="item-title">Larder Chili<span class="dots"></span>11.99</div><p class="item-desc">Chicken, onions, bell peppers, jalapeños, black &amp; kidney beans, and tomato.</p></div><div class="tags"><i class="tag gf"></i></div></div>
    <div class="item"><div class="item-body"><div class="item-title">Seasonal Rotating<span class="dots"></span>11.99</div><p class="item-desc">Butternut squash blended with warm spices, and coconut milk.</p></div><div class="tags"><i class="tag vegan"></i><i class="tag gf"></i></div></div>
    <div class="photo-row"><div class="photo ph-bowl" role="img" aria-label="Photo of a chicken and vegetable bowl"></div><div class="photo ph-soup" role="img" aria-label="Photo of a bowl of vegetable chili"></div></div>
  </div>

  <div class="panel">
    <h2 class="section-head">WRAPS</h2>
    <div class="item"><div class="item-body"><div class="item-title">Rancher's Wrap<span class="dots"></span>11.99</div><p class="item-desc">Tomato, red onion, hard boiled egg, avocado, feta cheese, microgreens, romaine, grilled chicken and Ranch dressing in a grilled wrap.</p></div><div class="tags"></div></div>
    <div class="item"><div class="item-body"><div class="item-title">Vegan Tuna Wrap<span class="dots"></span>11.99</div><p class="item-desc">Vegan tuna, romaine, avocado, celery, shallot, and oregano with Herbalicious Sauce in a whole grain wrap.</p></div><div class="tags"><i class="tag vegan"></i></div></div>
    <div class="item"><div class="item-body"><div class="item-title">Vegetarian Wrap<span class="dots"></span>11.99</div><p class="item-desc">Roasted chickpeas, romaine, avocado, red bell pepper, shaved carrots, cucumber, spinach, basil, black beans and feta with lemon-hummus in a sprouted 7-grain wrap.</p></div><div class="tags"><i class="tag veg"></i></div></div>
    <div class="photo-row"><div class="photo ph-wrap" role="img" aria-label="Photo of a spinach wrap cut in half"></div><div class="photo ph-salad" role="img" aria-label="Photo of a beet and avocado salad"></div></div>
    <h2 class="section-head gap">SALAD</h2>
    <div class="item"><div class="item-body"><div class="item-title">Avocado, Golden Beet, &amp; Cranberry Salad<span class="dots"></span>11.99</div><p class="item-desc">Gold beets, avocado, dried cranberries, watermelon radish, red kale, romaine, mixed greens, and pepitas served with Golden Buddha dressing.</p></div><div class="tags"><i class="tag gf"></i><i class="tag veg"></i></div></div>
    <div class="item"><div class="item-body"><div class="item-title">Burrata Salad<span class="dots"></span>11.99</div><p class="item-desc">Tomato, melon, shredded basil, balsamic glaze, fresh cracked pepper, and olive oil with burrata.</p></div><div class="tags"><i class="tag gf"></i><i class="tag veg"></i></div></div>
    <div class="item"><div class="item-body"><div class="item-title">Mediterranean Salad<span class="dots"></span>11.99</div><p class="item-desc">Cucumbers, Kalamata olives, cherry tomatoes, parsley, tricolor quinoa, hard-boiled egg, and hummus on mixed greens, romaine, and red cabbage with lemon-olive oil dressing.</p></div><div class="tags"><i class="tag gf"></i><i class="tag veg"></i></div></div>
    <div class="item"><div class="item-body"><div class="item-title">Vegan Chef Salad<span class="dots"></span>11.99</div><p class="item-desc">Roasted potatoes and carrots, chickpeas, avocado, microgreens and walnuts on mixed greens, romaine, and red kale with vegan ranch.</p></div><div class="tags"><i class="tag gf"></i><i class="tag nuts"></i></div></div>
    <div class="item"><div class="item-body"><div class="item-title">Rancher's Salad<span class="dots"></span>11.99</div><p class="item-desc">Tomato, red onion, hard boiled egg, avocado, feta cheese, microgreens, and grilled chicken on romaine with Ranch dressing.</p></div><div class="tags"><i class="tag gf"></i><i class="tag veg"></i></div></div>
  </div>

  <div class="panel">
    <h2 class="section-head">BURGERS N' SAMMIES</h2>
    <div class="item"><div class="item-body"><div class="item-title">Air Fried Chicken Sammy<span class="dots"></span>11.99</div><p class="item-desc">Air fried chicken breast topped with red leaf lettuce, tomato, house made pickles and Larder Sauce on a bun served with choice of salad or fries.</p></div><div class="tags"></div></div>
    <div class="item"><div class="item-body"><div class="item-title">Grilled Chicken Sammy<span class="dots"></span>11.99</div><p class="item-desc">Grilled chicken topped with guacamole, red leaf lettuce, tomato, house made pickles and Larder Sauce. Served with regular fries or side salad.</p></div><div class="tags"></div></div>
    <div class="item"><div class="item-body"><div class="item-title">Classic Beef Burger<span class="dots"></span>11.99</div><p class="item-desc">House seasoned beef burger topped with red leaf lettuce, tomato, cheddar cheese, house made pickles and Larder Sauce on a bun served with choice of salad of fries.</p></div><div class="tags"></div></div>
    <div class="item"><div class="item-body"><div class="item-title">Black Bean Pine Nut Burger<span class="dots"></span>11.99</div><p class="item-desc">House made black bean pine nut burger topped with red leaf lettuce, tomato, house made pickles and mustard aioli on a bun served with choice of salad of fries.</p></div><div class="tags"><i class="tag vegan"></i><i class="tag nuts"></i></div></div>
    <div class="item"><div class="item-body"><div class="item-title">Salmon Burger<span class="dots"></span>11.99</div><p class="item-desc">House made salmon burger topped with red leaf lettuce, tomato, house made pickles and Larder yogurt on a bun served with choice of salad of fries.</p></div><div class="tags"></div></div>
    <h2 class="section-head gap">SNACKS N' SIDES</h2>
    <div class="item"><div class="item-body"><div class="item-title">Fries<span class="dots"></span>11.99</div><p class="item-desc">Hand cut air-fries with house seasonings. Choose regular or sweet potato fries.</p></div><div class="tags"><i class="tag vegan"></i><i class="tag gf"></i></div></div>
    <div class="item"><div class="item-body"><div class="item-title">Side Salad<span class="dots"></span>11.99</div><p class="item-desc">Your choice of House, Golden Beet, Mediterranean, or Vegan Chef side salad. (24oz)</p></div><div class="tags"><i class="tag vegan"></i></div></div>
    <div class="item"><div class="item-body"><div class="item-title">Guac + Chips<span class="dots"></span>11.99</div><p class="item-desc">Guacamole with blue corn tortilla chips.</p></div><div class="tags"><i class="tag vegan"></i></div></div>
    <div class="item"><div class="item-body"><div class="item-title">Hummus + Chips<span class="dots"></span>11.99</div><p class="item-desc">Hummus with blue corn tortilla chips.</p></div><div class="tags"><i class="tag gf"></i></div></div>
    <div class="combos">
      <div class="combos-label">COMBOS</div>
      <div class="item-body">
        <div class="item"><div class="item-body"><div class="item-title">Soup + Salad<span class="dots"></span>11.99</div><p class="item-desc">Your choice of soup and side salad. 16oz soup + 38oz salad</p></div></div>
        <div class="item"><div class="item-body"><div class="item-title">Avo Toast Combo<span class="dots"></span>11.99</div><p class="item-desc">Half avocado toast and your choice of soup. 16oz</p></div></div>
        <div class="item"><div class="item-body"><div class="item-title">Soup + Sammy<span class="dots"></span>11.99</div><p class="item-desc">Your choice of soup and sandwich. 16oz soup + Sandwich</p></div></div>
      </div>
    </div>
  </div>
</section>

</body>
</html>
```